Paleo Diet Book Cover Design

I need a cover designed for my book Stone Frame that will be sold on Brightleaf Reader and other sites. So the front, side and back will need to be designed. I have attached part of the book here so feel free to skim through the content and give it a quick read to get a feel for what the book is about. Stone Frame is about eating the diet of the caveman (paleolithic era-paleo) and a 12 week workout plan with a grocery shopping list and meal plans. It is for men and women ages 18+ who are interested in health and fitness and becoming healthier overall.
The graphics should be secondary, and it should add to the text, not distract from it. This is even more important because the size of the cover displayed on Brightleaf/Reader, when your book is first seen by a potential buyer, is so tiny. It's barely an inch high, and even smaller in width.
So the words have to be big, bold, benefit-rich and easy to read. That also means, don't mess with the fancy fonts. Clean, clear, crisp font is best. And, did I say BIG already?
Contrast the colors of the text and background, so its even easier to read. That means, dark text on light background or visa versa. Colors like darker reds, blues / teals and oranges.
Please read this: http://www.jacketforge.net/8-cover-design-secrets-publishers-use-to-manipulate-readers-into-buying-books/
The cover has to be bold and easy to read, it has to stick out, it has to draw the attention of your readers so that they zero in on my book, out of all the other books on the page. (Much like they would when viewing a classified ads site/page.)
The Title of the Book is Stone Frame, and the subtitle is "Transform Your Body For Life in 12 Weeks With Proven Workouts and Paleo Diet Based Nutrition" Perhaps “Transform Your Body For Life in 12 Weeks” could also be in a large font similar to the title with the rest of the subtitle following afterwards. You can try having the title be the smaller font with the subtitle being the larger font as well.
Then the authors name "Martin Oakes” incorporated into the design.
I am not sure what to use as the background type of design for the front of the book so feel free to be creative with that.
The size needs to be 1563 pixels on the shortest side and 2500 pixels on the longest side just for the front of the cover.

```html
<!DOCTYPE html>
<html lang="en">
<head>
<meta charset="utf-8">
<title>Stone Frame — Book Cover</title>
<link rel="stylesheet" href="https://fonts.googleapis.com/css2?family=Fira+Sans:wght@600;700;800&display=swap">
<style>
  :root {
    --cover-blue: #17a9e4;
    --cover-blue-light: #2bb6ec;
    --cover-blue-dark: #0f9ad6;
    --ink: #000000;
  }
  * { margin: 0; padding: 0; box-sizing: border-box; }
  html, body {
    width: 750px;
    height: 1200px;
    overflow: hidden;
    background: var(--cover-blue);
  }
  .cover {
    position: relative;
    width: 750px;
    height: 1200px;
    overflow: hidden;
    font-family: "Fira Sans", Arial, sans-serif;
    color: var(--ink);
  }
  .cover-texture {
    position: absolute;
    inset: 0;
    background: linear-gradient(135deg, var(--cover-blue-light) 0%, var(--cover-blue) 50%, var(--cover-blue-dark) 100%);
  }
  .title {
    position: absolute;
    left: 0;
    top: 0;
    width: 750px;
    height: 520px;
  }
  .title text {
    font-family: "Fira Sans", Arial, sans-serif;
    font-weight: 700;
    fill: var(--ink);
  }
  .subtitle {
    position: absolute;
    left: 0;
    width: 750px;
    top: 556px;
    text-align: center;
  }
  .subtitle-lead {
    font-size: 41px;
    font-weight: 700;
    line-height: 56px;
    letter-spacing: 0.2px;
  }
  .subtitle-line {
    font-size: 32px;
    font-weight: 600;
    line-height: 60px;
  }
  .byline {
    position: absolute;
    left: 0;
    width: 750px;
    top: 1012px;
    text-align: center;
  }
  .byline-label {
    font-size: 34px;
    font-weight: 600;
    line-height: 44px;
  }
  .author {
    font-size: 48px;
    font-weight: 700;
    line-height: 70px;
    margin-top: 12px;
  }
</style>
</head>
<body>
  <main class="cover">
    <div class="cover-texture" role="img" aria-label="Brushed blue textured background"></div>

    <svg class="title" viewBox="0 0 750 520" aria-label="Stone Frame">
      <text x="52" y="240" font-size="222" textLength="660" lengthAdjust="spacingAndGlyphs">STONE</text>
      <text x="52" y="490" font-size="236" textLength="660" lengthAdjust="spacingAndGlyphs">FRAME</text>
    </svg>

    <section class="subtitle">
      <p class="subtitle-lead">Transform Your Body For Life</p>
      <p class="subtitle-line">in</p>
      <p class="subtitle-line">12 Weeks</p>
      <p class="subtitle-line">With</p>
      <p class="subtitle-line">Proven Workouts</p>
      <p class="subtitle-line">and</p>
      <p class="subtitle-line">Paleo Diet Based Nutrition</p>
    </section>

    <section class="byline">
      <p class="byline-label">Written by</p>
      <p class="author">MARTIN OAKES</p>
    </section>
  </main>
</body>
</html>
```